New professional looking flyer for company

I need our flyer updated my flyer is the Ruv flyer Have attached current flyer so you know what services need to be listed. Want it to be in mainly dark colours like black and dark grey with pops of light grey, silver or white. i have added several photos for you to choose which ones work best with your design would like The photos to be in colour for the flyer. But can have a mix of greyscale if that works for your design j have attached another companies flyers as design ideas to show what I am looking for

Target Market(s)

new clients

Industry/Entity Type

transport and earthmoving

Colors

Designer to choose colors to be used in the design.

Requirements
Nice to have
• Look professional
Should not have
• No orange or red or green

```html
<!DOCTYPE html>
<html lang="en">
<head>
<meta charset="utf-8">
<title>Ruv Pty Ltd – Our Services</title>
<link href="https://fonts.googleapis.com/css2?family=Rubik:wght@500;700;800&display=swap" rel="stylesheet">
<style>
  :root{
    --ink:#2b2b2d;
    --charcoal:#3a3a3c;
    --night:#232325;
    --slate:#55585d;
    --steel:#7d8187;
    --frame:#333335;
    --stone:#e4e5e7;
    --silver:#c9cbcf;
    --white:#ffffff;
    --gold:#e6ad12;
  }
  *{margin:0;padding:0;box-sizing:border-box}
  html,body{width:848px;height:1200px;overflow:hidden;background:var(--stone)}
  .flyer{position:relative;width:848px;height:1200px;overflow:hidden;font-family:"Rubik",Arial,sans-serif;background:var(--stone)}
  .backdrop{position:absolute;inset:0}
  .brand{position:absolute;left:622px;top:70px;width:186px;text-align:center;color:var(--silver)}
  .brand-rule{height:1px;background:var(--silver);opacity:.7}
  .brand-name{font-weight:800;font-size:70px;line-height:78px;letter-spacing:2px}
  .brand-sub{font-weight:800;font-size:16px;line-height:20px;letter-spacing:1px;margin-bottom:4px}
  .gallery{position:absolute;left:84px;top:620px;display:flex;gap:11px}
  .gallery .shot{width:163px;height:144px;background:var(--frame);padding:6px}
  .gallery .shot div{width:100%;height:100%}
  .services-title{position:absolute;top:792px;left:0;width:848px;display:flex;align-items:center;justify-content:center;gap:10px;color:var(--ink);font-weight:800;font-size:29px;letter-spacing:.5px}
  .services-title .rule{width:165px;height:1.5px;background:var(--ink);position:relative}
  .services-title .rule.l::after,.services-title .rule.r::before{content:"";position:absolute;top:-3px;width:7px;height:7px;border-radius:50%;background:var(--ink)}
  .services-title .rule.l::after{right:-4px}
  .services-title .rule.r::before{left:-4px}
  .service-list{position:absolute;top:844px;list-style:none;color:var(--ink);font-weight:700;font-size:16px;letter-spacing:.6px}
  .service-list li{height:23.6px;line-height:23.6px;position:relative;padding-left:18px}
  .service-list li::before{content:"";position:absolute;left:0;top:11px;width:3.5px;height:3.5px;border-radius:50%;background:var(--ink)}
  .service-list.left{left:78px}
  .service-list.right{left:511px}
  .services-divider{position:absolute;left:481px;top:850px;width:1.5px;height:160px;background:var(--ink)}
  .contact{position:absolute;left:73px;top:1058px;color:var(--white)}
  .contact .note{font-weight:700;font-size:8.5px;letter-spacing:.2px}
  .contact .cta{color:var(--gold);font-weight:700;font-size:12.5px;line-height:13px;margin-top:4px;letter-spacing:.3px}
  .contact .cta.big{font-size:15px;line-height:15px;margin-top:0}
  .phone{position:absolute;left:76px;top:1108px;display:flex;align-items:center;gap:6px;color:var(--white);font-weight:800;font-size:39px;letter-spacing:1px}
  .address{position:absolute;left:73px;top:1160px;display:flex;align-items:center;gap:8px;color:var(--gold);font-weight:700;font-size:11.8px;letter-spacing:.4px}
  .signoff{position:absolute;right:69px;top:1134px;text-align:right;font-weight:700;font-size:17.5px;line-height:24px}
  .signoff .company{color:var(--white)}
  .signoff .email{color:var(--gold)}
</style>
</head>
<body>
<div class="flyer">
  <svg class="backdrop" width="848" height="1200" viewBox="0 0 848 1200">
    <defs>
      <linearGradient id="heroTone" x1="0" y1="0" x2="0" y2="1">
        <stop offset="0" stop-color="#2c2c2e"/>
        <stop offset=".2" stop-color="#45484d"/>
        <stop offset=".38" stop-color="#6d7278"/>
        <stop offset=".55" stop-color="#8e9399"/>
        <stop offset=".78" stop-color="#4a4c50"/>
        <stop offset="1" stop-color="#2a2a2c"/>
      </linearGradient>
      <linearGradient id="gravelTone" x1="0" y1="0" x2="1" y2="1">
        <stop offset="0" stop-color="#c6c8cb"/>
        <stop offset="1" stop-color="#9ea1a5"/>
      </linearGradient>
    </defs>
    <g role="img" aria-label="Photo of a white prime mover truck on an outback road at dusk">
      <polygon points="0,0 848,0 848,420 410,622 0,790" fill="url(#heroTone)"/>
    </g>
    <g role="img" aria-label="Photo of crushed gravel and packed earth">
      <polygon points="420,622 848,428 848,680 760,680 760,620 420,640" fill="url(#gravelTone)"/>
      <polygon points="590,620 848,530 848,676 590,676" fill="var(--slate)"/>
    </g>
    <polygon points="395,626 848,418 848,434 430,626" fill="var(--gold)"/>
    <polygon points="0,780 95,760 95,766 0,790" fill="var(--gold)"/>
    <polygon points="0,996 848,1082 848,1200 0,1200" fill="var(--charcoal)"/>
    <polygon points="0,982 848,1068 848,1082 0,998" fill="var(--gold)"/>
  </svg>

  <div class="brand">
    <div class="brand-rule"></div>
    <div class="brand-name">Ruv</div>
    <div class="brand-sub">Pty Ltd</div>
    <div class="brand-rule"></div>
  </div>

  <div class="gallery">
    <div class="shot"><div role="img" aria-label="Excavator trenching beside a truck" style="background:linear-gradient(#6f8aa8,#5b5e63 60%,#3f4144)"></div></div>
    <div class="shot"><div role="img" aria-label="Freshly graded dirt road" style="background:linear-gradient(#8fa2b5,#7b7e83 45%,#66696d)"></div></div>
    <div class="shot"><div role="img" aria-label="Loader filling a road train tipper" style="background:linear-gradient(#5d7ea4,#8a9097 55%,#55585c)"></div></div>
    <div class="shot"><div role="img" aria-label="Truck carrying a loader on a drop deck trailer" style="background:linear-gradient(#a3b3c2,#c9cdd2 50%,#6a6d71)"></div></div>
  </div>

  <h2 class="services-title"><span class="rule l"></span>OUR SERVICES<span class="rule r"></span></h2>

  <ul class="service-list left">
    <li>OVER SIZE LOADS / HOT SHOT LOADS</li>
    <li>HEAVY VEHICLE RECOVERY SERVICES</li>
    <li>POTABLE WATER DELIVERIES</li>
    <li>ROAD BUILDING / MAINTENANCE</li>
    <li>EARTHWORKS</li>
    <li>SAND &amp; METAL SUPPLY &amp; CARTAGE</li>
  </ul>
  <div class="services-divider"></div>
  <ul class="service-list right">
    <li>ROAD TRAIN TIPPERS</li>
    <li>ROAD TRAIN TANKERS</li>
    <li>ROAD TRAIN FLAT TOPS</li>
    <li>DROP DECK TRAILERS</li>
    <li>MINE SITE ACCREDITED</li>
    <li>EQUIPMENT &amp; OPERATORS</li>
    <li>TRAFFIC MANAGEMENT</li>
  </ul>

  <div class="contact">
    <p class="note">WE OFFER A LARGE RANGE OF SERVICES NOT LISTED SO</p>
    <p class="cta">CALL US TODAY FOR A PERSONALISED</p>
    <p class="cta big">QUOTE TO SUIT YOUR NEEDS.</p>
  </div>

  <div class="phone">
    <svg width="18" height="28" viewBox="0 0 18 28"><rect x="1.5" y="1.5" width="15" height="25" rx="2.5" fill="none" stroke="#fff" stroke-width="2"/><line x1="1.5" y1="21" x2="16.5" y2="21" stroke="#fff" stroke-width="2"/></svg>
    <span>1300 555 018</span>
  </div>

  <div class="address">
    <svg width="13" height="17" viewBox="0 0 13 17"><path d="M6.5 0A6.5 6.5 0 0 0 0 6.5C0 11 6.5 17 6.5 17S13 11 13 6.5A6.5 6.5 0 0 0 6.5 0z" fill="#fff"/><circle cx="6.5" cy="6.3" r="2.4" fill="#3a3a3c"/></svg>
    <span>LEVEL 4 28 HARBOUR STREET RIVERTON 2150. AUSTRALIA.</span>
  </div>

  <div class="signoff">
    <div class="company">Ruv Pty Ltd</div>
    <div class="email">info@ruv.com.au</div>
  </div>
</div>
</body>
</html>
```